Business Card Design Project 4 Construction Business

I am after a creative, but sleek and simple/ clean business card design. This design will form the basis of future items and might include a logo or simply a creative way to lay out the text of my company name 'kestrel ventures'
I like the simplicity of black and white however I would also be happy to see a splash of colour introduced somehow to give the text some interest and make it stand out.
I would like a double sided card.
I am young (ish!) and professional, offering construction and project management services, what I don't want is the traditional builders type card featuring a cheesy hammer/ saw image etc.
As the company name, kestrel ventures, suggests, we focus on working closely and collaboratively together, in synergy with all stakeholders involved in the projects that we undertake
Construction

```html
<!DOCTYPE html>
<html lang="en">
<head>
<meta charset="utf-8">
<title>Kestrel Ventures – Business Card</title>
<link rel="stylesheet" href="https://fonts.googleapis.com/css2?family=Arimo:wght@400;700&display=swap">
<style>
  :root {
    --brand-blue: #0a7bb8;
    --card-white: #ffffff;
    --page-bg: #e4e4e4;
    --ink-white: #ffffff;
  }
  * { box-sizing: border-box; margin: 0; padding: 0; }
  html, body {
    width: 1200px;
    height: 1000px;
    overflow: hidden;
  }
  body {
    background: var(--page-bg);
    font-family: "Arimo", Arial, sans-serif;
    position: relative;
  }
  .card {
    position: absolute;
    width: 600px;
    height: 343px;
    box-shadow: 0 2px 6px rgba(0,0,0,0.18);
    overflow: hidden;
  }

  /* Front side */
  .card-front {
    left: 90px;
    top: 110px;
    background: var(--brand-blue);
    color: var(--ink-white);
  }
  .card-front .wordmark {
    position: absolute;
    left: 0; right: 0;
    top: 146px;
    text-align: center;
    font-weight: 700;
    font-size: 38px;
    letter-spacing: 3px;
  }
  .card-front .web {
    position: absolute;
    right: 26px;
    bottom: 20px;
    font-size: 16px;
    font-weight: 400;
  }

  /* Back side */
  .card-back {
    left: 510px;
    top: 530px;
    background: var(--card-white);
    color: var(--brand-blue);
  }
  .card-back .wordmark {
    position: absolute;
    right: 26px;
    top: 30px;
    font-weight: 700;
    font-size: 24px;
    letter-spacing: 2px;
  }
  .card-back .person {
    position: absolute;
    left: 46px;
    top: 84px;
  }
  .person .name {
    font-weight: 700;
    font-size: 30px;
    letter-spacing: 2px;
    line-height: 1;
  }
  .person .role {
    font-size: 15px;
    margin-top: 3px;
  }
  .contacts {
    position: absolute;
    left: 42px;
    top: 166px;
    list-style: none;
  }
  .contacts li {
    display: flex;
    align-items: center;
    gap: 12px;
    height: 34px;
    font-weight: 700;
    font-size: 14px;
    letter-spacing: 1.2px;
  }
  .contacts svg { width: 24px; height: 24px; flex: none; }
  .address-band {
    position: absolute;
    left: 0; right: 0; bottom: 0;
    height: 68px;
    background: var(--brand-blue);
    color: var(--ink-white);
    display: flex;
    align-items: center;
    justify-content: center;
    font-size: 19px;
  }
</style>
</head>
<body>

  <section class="card card-front" aria-label="Card front">
    <div class="wordmark">KESTREL VENTURES</div>
    <div class="web">www.kestrelventuresgroup.com.au</div>
  </section>

  <section class="card card-back" aria-label="Card back">
    <div class="wordmark">KESTREL VENTURES</div>
    <div class="person">
      <div class="name">Tom Hadley</div>
      <div class="role">Director</div>
    </div>
    <ul class="contacts">
      <li>
        <svg viewBox="0 0 24 24" aria-hidden="true">
          <rect width="24" height="24" rx="3" fill="var(--brand-blue)"/>
          <path d="M7 5c1-.6 2 .2 2.5 1.5l.6 1.8c.2.7-.2 1.2-.8 1.6l-.6.4c.6 1.8 1.9 3.4 3.6 4.4l.5-.6c.4-.5 1-.8 1.6-.5l1.8.8c1.2.6 1.8 1.6 1.1 2.5-.9 1.3-2.4 1.8-3.9 1.2C9 16.6 6.3 12.9 5.8 8.6 5.6 7 6 5.7 7 5z" fill="var(--card-white)"/>
        </svg>
        0400 555 019
      </li>
      <li>
        <svg viewBox="0 0 24 24" aria-hidden="true">
          <rect width="24" height="24" rx="3" fill="var(--brand-blue)"/>
          <text x="12" y="18.5" text-anchor="middle" font-family="Arimo, Arial, sans-serif" font-weight="700" font-size="19" fill="var(--card-white)">e</text>
        </svg>
        tom@kestrelventuresgroup.com.au
      </li>
      <li>
        <svg viewBox="0 0 24 24" aria-hidden="true">
          <rect width="24" height="24" rx="3" fill="var(--brand-blue)"/>
          <g fill="none" stroke="var(--card-white)" stroke-width="1.4">
            <circle cx="12" cy="12" r="8"/>
            <ellipse cx="12" cy="12" rx="3.6" ry="8"/>
            <line x1="4" y1="12" x2="20" y2="12"/>
            <path d="M5.5 8h13M5.5 16h13"/>
          </g>
        </svg>
        www.kestrelventuresgroup.com.au
      </li>
    </ul>
    <div class="address-band">Address: 12 Carden Rd Eastbrook NSW 2999</div>
  </section>

</body>
</html>
```